Australian Craft Distillery needs poster layout for its awesome Manifesto

Tall Finch's a small craft distillery based in the Brook Flats of Western Australia producing award-winning vodkas and gin. Check out our website www.tallfinchs-example.com.au to get a feel for our design aesthetic, especially from our bottle design. We are "Small Batch Liquors - Out of the Brook Flats". Everything we do reflects that.
We have a manifesto - The Tall Finch's Manifesto -that we proudly display in our tasting room, and was used as a basis for an artwork in our entry.
We've had a number of customers ask to buy a poster of the manifesto (attached) so I want to commission a more professional design than the current layout which was put together in Word! (yes I know, I'm sorry, I did move it into Illustrator later).
I think the text flows in a sequential order so I'm looking for a design that you read from start to finish rather than a random collection of statements. I'd like to include our logo in the design somewhere but it doesn't have to be front and centre. There is a secondary logo device as well - the interlocked T and F on the label which could be used. I'm assuming the print will be simple black on either a plain background or a "craft background" similar to the labels. Our current fonts are SchmutzICG for text and VeneerTwo for headings. The label uses Haymaker and Gin-Rough.
Print size will be A3 (prefer the design to be to this proportion and portrait orientation) and bigger up to A1. We'll print the final design on the back of t-shirts for staff as well. If I was going to sum up our style in a couple of words it would be "intelligently irreverent" Have fun with this, I certainly did writing it!

```html
<!DOCTYPE html>
<html lang="en">
<head>
<meta charset="utf-8">
<title>The Tall Finch's Manifesto</title>
<link rel="stylesheet" href="https://fonts.googleapis.com/css2?family=Rye&family=Patrick+Hand&display=swap">
<style>
  :root {
    --paper: #f1e7d0;
    --paper-edge: #e4d4b3;
    --ink: #5b3f2f;
    --frame: #6b4a37;
    --photo-wall: #b9ad98;
    --photo-board: #3a3532;
  }
  * { margin: 0; padding: 0; box-sizing: border-box; }
  html, body { width: 849px; height: 1200px; overflow: hidden; }
  body {
    background: radial-gradient(ellipse at 50% 40%, var(--paper) 55%, var(--paper-edge) 100%);
    color: var(--ink);
    font-family: "Patrick Hand", cursive;
  }
  .poster { position: relative; width: 849px; height: 1200px; }

  .brand-mark {
    position: absolute; top: 48px; left: 0; width: 100%;
    display: flex; justify-content: center; align-items: center; gap: 10px;
    font-family: "Rye", serif; font-size: 34px; color: var(--ink);
  }
  .brand-mark .dot { width: 14px; height: 14px; border: 2px solid var(--ink); border-radius: 50%; }

  .title {
    position: absolute; top: 150px; width: 100%; text-align: center;
    font-family: "Rye", serif; font-weight: 400; font-size: 38px; letter-spacing: 1px;
  }
  .subtitle {
    position: absolute; top: 203px; width: 100%; text-align: center;
    font-size: 23px;
  }

  .heading {
    position: absolute; font-family: "Rye", serif; font-weight: 400;
    font-size: 36px; letter-spacing: 1px; line-height: 1;
  }
  .list { position: absolute; list-style: none; font-size: 17.5px; line-height: 25px; }

  .first-heading { top: 268px; left: 0; width: 100%; text-align: center; }
  .first-list { top: 313px; left: 0; width: 100%; text-align: center; }

  .then-heading { top: 478px; right: 96px; }
  .then-list { top: 523px; right: 55px; text-align: right; }

  .finally-heading { top: 818px; left: 80px; }
  .finally-list { top: 862px; left: 80px; }

  .photo {
    position: absolute; border: 9px solid var(--frame);
    box-shadow: 0 2px 6px rgba(60, 40, 25, 0.35);
  }
  .photo-tasting-room {
    left: 50px; top: 456px; width: 262px; height: 330px;
    background: linear-gradient(160deg, #d9d2c4 0%, var(--photo-wall) 55%, #7a6652 100%);
    transform: rotate(-2.5deg);
  }
  .photo-chalkboard {
    left: 512px; top: 782px; width: 292px; height: 346px;
    background: linear-gradient(200deg, #a88f78 0%, var(--photo-board) 35%, #242120 100%);
    transform: rotate(2.5deg);
  }
</style>
</head>
<body>
<main class="poster">
  <div class="brand-mark"><span class="dot"></span>Tall Finch's</div>

  <h1 class="title">THE TALL FINCH'S MANIFESTO</h1>
  <p class="subtitle">(our thoughts on life, a.k.a. how to be better)</p>

  <h2 class="heading first-heading">FIRST</h2>
  <ul class="list first-list">
    <li>• Work Smart • Love Hard •</li>
    <li>•Play Often • Sleep More •</li>
    <li>• Stay Present • Be Local •</li>
    <li>• Embrace Silly • Get Dirty (but) Stay Clean •</li>
    <li>• Laugh • Cry • Run • Dance • Sing •</li>
    <li>• Stop That (and) Slow down •</li>
  </ul>

  <div class="photo photo-tasting-room" role="img" aria-label="Photo of the tasting room wall with the manifesto painted on it, a teal creature sculpture, a barrel and a steel still"></div>

  <h2 class="heading then-heading">THEN</h2>
  <ul class="list then-list">
    <li>• Celebrate others success • Don't be shit •</li>
    <li>• Have one thing you are awesome at •</li>
    <li>• Get off your phone • Show some fucking passion •</li>
    <li>• Make something •</li>
    <li>• Making money doesn't count • Making babies does •</li>
    <li>• Never stop exploring, never stop learning, share that with others •</li>
    <li>• We all fuck up. Make good, learn, be better and move on •</li>
    <li>• Life is far too short, squeeze every drop out of it •</li>
    <li>and, of course …</li>
    <li>• Drink better •</li>
  </ul>

  <h2 class="heading finally-heading">AND FINALLY</h2>
  <ul class="list finally-list">
    <li>• Sometimes you just won't understand •</li>
    <li>• An argument is not a fight •</li>
    <li>• You are not as important as you think •</li>
    <li>• You are more loved than you think •</li>
    <li>• Its ok to do things alone •</li>
    <li>• Its ok not to be busy •</li>
    <li>• There is no good reason to do a half arsed job •</li>
    <li>• Teaching is the best way of learning •</li>
    <li>• The past is important, what you do next is much more so •</li>
    <li>• Change is inevitable, roll with it •</li>
    <li>• Success is whatever you decide it to be •</li>
  </ul>

  <div class="photo photo-chalkboard" role="img" aria-label="Photo of a wooden-framed chalkboard with a chalk to-do list: make booze, be awesome"></div>
</main>
</body>
</html>
```